Relocation/furniture installation company needs new business cards

we are a relocation and furniture installation company mainly dealing with corporate clients and we are looking for new business card ideas. Cards should incorporate our logo and list our website, phone number and services. The company is only 2 years old but with more staff joining we are in the need for more business cards, so something with an awesome design that is eye catching would go a long way to insure we get our name out there and look good to potential new clients.

Target Market(s)

Corporate

Industry/Entity Type

Trade

Contact Information for Business Card

www.mervoline.co.nz
0508 4 bravok

furniture installation
business relocations
joinery installation
commercial property maintenance

Colors
0592cd
34a7d8
85cae6
85acd3
0356a4
cfdfed
cee9f5
757575
474747

Requirements
Must have
• Business relocations and furniture installation specialists
Nice to have
• something that incorporates our logo.

```html
<!DOCTYPE html>
<html lang="en">
<head>
<meta charset="utf-8">
<title>Mervoline business cards</title>
<link href="https://fonts.googleapis.com/css2?family=Open+Sans:wght@400;600&family=Russo+One&display=swap" rel="stylesheet">
<style>
  :root {
    --backdrop: #676767;
    --card: #f7f7f5;
    --navy: #2e3690;
    --cyan: #1ea8dc;
    --steel: #356aa2;
    --sky: #0592cd;
    --white: #ffffff;
  }
  * { margin: 0; padding: 0; box-sizing: border-box; }
  html, body { width: 1200px; height: 1011px; overflow: hidden; }
  body { background: var(--backdrop); position: relative; font-family: "Open Sans", sans-serif; }
  .card { position: absolute; left: 357px; width: 486px; height: 293px; background: var(--card); overflow: hidden; }
  .card--front { top: 186px; }
  .card--back { top: 532px; }

  .wordmark { position: absolute; font-family: "Russo One", sans-serif; color: var(--navy); letter-spacing: 4px; white-space: nowrap; line-height: 1; }
  .card--front .wordmark { left: 0; width: 486px; top: 168px; text-align: center; font-size: 36px; }
  .card--back .wordmark { left: 20px; top: 158px; font-size: 33px; letter-spacing: 3.5px; }

  .tagline { position: absolute; left: 0; width: 486px; top: 216px; text-align: center; font-size: 10.5px; letter-spacing: 1.2px; color: var(--steel); text-transform: uppercase; }

  .site-rule { position: absolute; top: 266px; left: 30px; width: 426px; height: 14px; }
  .site-line { position: absolute; top: 264px; left: 0; width: 486px; text-align: center; font-size: 11.5px; letter-spacing: 2.4px; color: var(--navy); }
  .site-line .accent { color: var(--sky); }

  .person { position: absolute; right: 24px; top: 48px; text-align: right; }
  .person__name { font-family: "Russo One", sans-serif; font-size: 23px; color: var(--navy); letter-spacing: 1px; line-height: 1.1; }
  .person__role { font-size: 12.5px; color: var(--navy); margin-top: 6px; }

  .waves { position: absolute; left: 0; top: 0; width: 486px; height: 293px; }

  .contacts { position: absolute; right: 24px; top: 216px; list-style: none; }
  .contacts li { display: flex; align-items: center; justify-content: flex-end; gap: 8px; height: 19.5px; font-size: 12.5px; color: var(--white); }
  .contacts svg { width: 10px; height: 10px; }
</style>
</head>
<body>

<section class="card card--front">
  <div class="wordmark">MERVOLINE</div>
  <div class="tagline">Business relocations &amp; furniture installation specialists</div>
  <svg class="site-rule" viewBox="0 0 426 14" aria-hidden="true">
    <polygon points="0,7 119,3 119,11" fill="var(--navy)"/>
    <polygon points="426,7 308,3 308,11" fill="var(--navy)"/>
  </svg>
  <div class="site-line">www.<span class="accent">mervoline</span>.co.nz</div>
</section>

<section class="card card--back">
  <div class="wordmark">MERVOLINE</div>

  <div class="person">
    <div class="person__name">AARON KEALY</div>
    <div class="person__role">Managing Director</div>
  </div>

  <svg class="waves" viewBox="0 0 607 366" preserveAspectRatio="none" aria-hidden="true">
    <defs>
      <linearGradient id="ribbon" x1="0" y1="0" x2="1" y2="0">
        <stop offset="0" stop-color="var(--steel)"/>
        <stop offset="0.45" stop-color="#2a86c0"/>
        <stop offset="1" stop-color="var(--cyan)"/>
      </linearGradient>
    </defs>
    <path d="M0,345 C110,372 230,362 340,312 C440,264 520,214 607,214 L607,366 L0,366 Z" fill="var(--navy)"/>
    <path d="M0,294 C90,336 215,342 325,292 C430,242 520,190 607,192 L607,205 C520,204 440,254 335,302 C225,352 100,360 0,331 Z" fill="url(#ribbon)"/>
    <path d="M48,312 C140,330 230,328 318,298 C230,322 140,326 48,312 Z" fill="var(--card)"/>
  </svg>

  <ul class="contacts">
    <li>0508 4 bravok
      <svg viewBox="0 0 10 10"><path d="M1,4 C1,1 9,1 9,4 L7,4 L7,3 L3,3 L3,4 Z M2,5 L8,5 L9,9 L1,9 Z" fill="var(--sky)"/></svg>
    </li>
    <li>www.mervoline.co.nz
      <svg viewBox="0 0 10 10"><rect x="0.5" y="2" width="9" height="6" fill="var(--sky)"/><path d="M0.5,2 L5,5.5 L9.5,2" fill="none" stroke="var(--white)" stroke-width="0.8"/></svg>
    </li>
    <li>aaron@mervoline.co.nz
      <svg viewBox="0 0 10 10"><circle cx="5" cy="5" r="4.3" fill="var(--sky)"/><path d="M0.7,5 H9.3 M5,0.7 V9.3" stroke="var(--navy)" stroke-width="0.6"/></svg>
    </li>
  </ul>
</section>

</body>
</html>
```